New E-Learning Website Design Wanted!

I am creating an E-learning website for those interested in getting certifications in the IT industry.
For example, courses related to BKX, Pellin, RTM certifications and national certifications in the IT industry in Japan will be offered.
You can think of sites such as Pindoval, Fevly, VexaPoint, Bintorum.
But I am targeting industries in Japan at the moment.
Also, I have uploaded screenshots of pages that I think are good.

The company is Solvik Data
I recently got my company logo designed so I attached pdf file to this project brief.
I would appreciate it if you can make the site match the color scheme of the logo.

Target Market(s)

I am targeting individuals as well as large IT companies in Japan

Industry/Entity Type

Education

Coding

Coded - Design and coding required

Number of Pages Required

4 page

Font styles to use
Sans Serif

Colors

Designer to choose colors to be used in the design.

Requirements
Must have
• One top page design
• One course page (https://vexapt.test/courses/pellor-grid-systems)
• One learning page(where the learner can see the video)
• One blog page(https://news.vexapt.test/resources?_ga=2.36414185.89678801.1578174478-594719062.1578174478)
Nice to have
• Pricing page

```html
<!DOCTYPE html>
<html lang="en">
<head>
<meta charset="UTF-8">
<title>Solvik Data — Blog</title>
<link href="https://fonts.googleapis.com/css2?family=Montserrat:wght@400;500;600;700;800&display=swap" rel="stylesheet">
<style>
  :root{
    --navy:#1d2a5b;
    --navy-deep:#15204a;
    --accent:#ef5f5a;
    --coral:#f9675f;
    --text:#2a2f45;
    --muted:#6b7085;
    --line:#e3e5ec;
    --bg:#ffffff;
    --photo-a:#2b3a63;
    --photo-b:#4c5a80;
  }
  *{box-sizing:border-box;margin:0;padding:0}
  html,body{width:721px;height:1200px;overflow:hidden;background:var(--bg)}
  body{font-family:"Montserrat",sans-serif;color:var(--text);position:relative}

  .site-header{position:absolute;left:0;top:0;width:721px;height:30px;display:flex;align-items:center;padding:0 14px;box-shadow:0 1px 3px rgba(0,0,0,.06)}
  .brand{display:flex;align-items:center;gap:5px;font-size:9px;font-weight:600;color:var(--navy)}
  .brand-mark{width:10px;height:10px;border-radius:50%;background:var(--navy)}
  .main-nav{margin-left:auto;display:flex;align-items:center;gap:20px;font-size:8px;font-weight:500;color:var(--navy)}
  .main-nav .active{color:var(--accent)}
  .nav-auth{display:flex;align-items:center;gap:14px;margin-left:30px;font-size:8px;font-weight:600;color:var(--navy)}
  .btn-signup{background:var(--navy);color:#fff;padding:4px 14px;border-radius:2px}

  .section-title{position:absolute;left:62px;font-size:19px;font-weight:800;color:var(--navy)}

  .popular{position:absolute;left:62px;top:96px;width:596px;height:312px}
  .story{position:absolute;overflow:hidden;background:linear-gradient(160deg,var(--photo-b),var(--photo-a))}
  .story::after{content:"";position:absolute;inset:0;background:linear-gradient(180deg,rgba(21,32,74,0) 55%,rgba(21,32,74,.75))}
  .story-caption{position:absolute;left:9px;right:9px;bottom:8px;z-index:1;color:#fff;font-size:8px;font-weight:700;white-space:nowrap;overflow:hidden;text-overflow:ellipsis}
  .story-lead{left:0;top:0;width:288px;height:312px}
  .story-wide{left:303px;top:0;width:293px;height:154px}
  .story-small-a{left:303px;top:162px;width:140px;height:150px}
  .story-small-b{left:458px;top:162px;width:138px;height:150px}

  .latest-grid{position:absolute;left:62px;top:480px;display:grid;grid-template-columns:repeat(3,180px);grid-auto-rows:184px;column-gap:27px;row-gap:28px}
  .card{background:#fff;box-shadow:0 1px 6px rgba(20,30,70,.16);display:flex;flex-direction:column}
  .card-media{height:78px;background:var(--coral)}
  .card-body{padding:8px 8px 0}
  .card-title{font-size:8.5px;font-weight:700;color:var(--navy);white-space:nowrap;overflow:hidden;text-overflow:ellipsis}
  .card-text{margin-top:5px;font-size:5.6px;line-height:1.55;color:var(--muted)}
  .card-author{display:flex;align-items:center;gap:5px;margin-top:auto;padding:0 8px 8px;font-size:6px;color:var(--text)}
  .avatar{width:9px;height:9px;border-radius:50%;background:var(--navy)}

  .site-footer{position:absolute;left:0;top:1108px;width:721px;height:92px;border-top:1px solid var(--line)}
  .footer-row{position:absolute;left:62px;right:62px;top:24px;display:flex;align-items:center}
  .footer-nav{display:flex;gap:16px;margin-left:34px;font-size:7px;font-weight:500;color:var(--navy)}
  .social{margin-left:auto;display:flex;gap:8px}
  .social span{width:11px;height:11px;background:var(--accent);border-radius:2px}
  .copyright{position:absolute;left:0;right:0;top:70px;text-align:center;font-size:6.5px;color:var(--text)}
</style>
</head>
<body>
  <header class="site-header">
    <div class="brand"><span class="brand-mark"></span>Solvik Data</div>
    <nav class="main-nav">
      <span>Learning</span>
      <span class="active">Blog</span>
      <span>Course Sales</span>
      <span>Subscription</span>
    </nav>
    <div class="nav-auth">
      <span>Sign In</span>
      <span class="btn-signup">Sign Up</span>
    </div>
  </header>

  <h2 class="section-title" style="top:56px">Popular Stories</h2>
  <section class="popular">
    <article class="story story-lead" role="img" aria-label="Photo of students attending a class in a lecture room">
      <p class="story-caption">Lorem ipsum dolor sit amet, consectetur adipiscing elit...</p>
    </article>
    <article class="story story-wide" role="img" aria-label="Photo of colleagues discussing at a desk">
      <p class="story-caption">Lorem ipsum dolor sit amet, consectetur adipiscing elit...</p>
    </article>
    <article class="story story-small-a" role="img" aria-label="Photo of hands working on a laptop">
      <p class="story-caption">Lorem ipsum dolor sit amet...</p>
    </article>
    <article class="story story-small-b" role="img" aria-label="Photo of a notebook and pen on a desk">
      <p class="story-caption">Lorem ipsum dolor sit amet...</p>
    </article>
  </section>

  <h2 class="section-title" style="top:434px">Latest Stories</h2>
  <section class="latest-grid">
    <article class="card"><div class="card-media" role="img" aria-label="Article cover image"></div><div class="card-body"><h3 class="card-title">Lorem ipsum dolor sit amet, consectetur</h3><p class="card-text">Lorem ipsum dolor sit amet, consectetur adipiscing elit. Etiam efficitur libero et tempus vulputate. Nam vel elementum elit. Duis blandit non dui nec molestie. Fusce rutrum finibus laoreet. Nullam tempor lorem vitae pretium.</p></div><div class="card-author"><span class="avatar"></span>Author Name</div></article>
    <article class="card"><div class="card-media" role="img" aria-label="Article cover image"></div><div class="card-body"><h3 class="card-title">Lorem ipsum dolor sit amet, consectetur</h3><p class="card-text">Lorem ipsum dolor sit amet, consectetur adipiscing elit. Etiam efficitur libero et tempus vulputate. Nam vel elementum elit. Duis blandit non dui nec molestie. Fusce rutrum finibus laoreet. Nullam tempor lorem vitae pretium.</p></div><div class="card-author"><span class="avatar"></span>Author Name</div></article>
    <article class="card"><div class="card-media" role="img" aria-label="Article cover image"></div><div class="card-body"><h3 class="card-title">Lorem ipsum dolor sit amet, consectetur</h3><p class="card-text">Lorem ipsum dolor sit amet, consectetur adipiscing elit. Etiam efficitur libero et tempus vulputate. Nam vel elementum elit. Duis blandit non dui nec molestie. Fusce rutrum finibus laoreet. Nullam tempor lorem vitae pretium.</p></div><div class="card-author"><span class="avatar"></span>Author Name</div></article>
    <article class="card"><div class="card-media" role="img" aria-label="Article cover image"></div><div class="card-body"><h3 class="card-title">Lorem ipsum dolor sit amet, consectetur</h3><p class="card-text">Lorem ipsum dolor sit amet, consectetur adipiscing elit. Etiam efficitur libero et tempus vulputate. Nam vel elementum elit. Duis blandit non dui nec molestie. Fusce rutrum finibus laoreet. Nullam tempor lorem vitae pretium.</p></div><div class="card-author"><span class="avatar"></span>Author Name</div></article>
    <article class="card"><div class="card-media" role="img" aria-label="Article cover image"></div><div class="card-body"><h3 class="card-title">Lorem ipsum dolor sit amet, consectetur</h3><p class="card-text">Lorem ipsum dolor sit amet, consectetur adipiscing elit. Etiam efficitur libero et tempus vulputate. Nam vel elementum elit. Duis blandit non dui nec molestie. Fusce rutrum finibus laoreet. Nullam tempor lorem vitae pretium.</p></div><div class="card-author"><span class="avatar"></span>Author Name</div></article>
    <article class="card"><div class="card-media" role="img" aria-label="Article cover image"></div><div class="card-body"><h3 class="card-title">Lorem ipsum dolor sit amet, consectetur</h3><p class="card-text">Lorem ipsum dolor sit amet, consectetur adipiscing elit. Etiam efficitur libero et tempus vulputate. Nam vel elementum elit. Duis blandit non dui nec molestie. Fusce rutrum finibus laoreet. Nullam tempor lorem vitae pretium.</p></div><div class="card-author"><span class="avatar"></span>Author Name</div></article>
    <article class="card"><div class="card-media" role="img" aria-label="Article cover image"></div><div class="card-body"><h3 class="card-title">Lorem ipsum dolor sit amet, consectetur</h3><p class="card-text">Lorem ipsum dolor sit amet, consectetur adipiscing elit. Etiam efficitur libero et tempus vulputate. Nam vel elementum elit. Duis blandit non dui nec molestie. Fusce rutrum finibus laoreet. Nullam tempor lorem vitae pretium.</p></div><div class="card-author"><span class="avatar"></span>Author Name</div></article>
    <article class="card"><div class="card-media" role="img" aria-label="Article cover image"></div><div class="card-body"><h3 class="card-title">Lorem ipsum dolor sit amet, consectetur</h3><p class="card-text">Lorem ipsum dolor sit amet, consectetur adipiscing elit. Etiam efficitur libero et tempus vulputate. Nam vel elementum elit. Duis blandit non dui nec molestie. Fusce rutrum finibus laoreet. Nullam tempor lorem vitae pretium.</p></div><div class="card-author"><span class="avatar"></span>Author Name</div></article>
    <article class="card"><div class="card-media" role="img" aria-label="Article cover image"></div><div class="card-body"><h3 class="card-title">Lorem ipsum dolor sit amet, consectetur</h3><p class="card-text">Lorem ipsum dolor sit amet, consectetur adipiscing elit. Etiam efficitur libero et tempus vulputate. Nam vel elementum elit. Duis blandit non dui nec molestie. Fusce rutrum finibus laoreet. Nullam tempor lorem vitae pretium.</p></div><div class="card-author"><span class="avatar"></span>Author Name</div></article>
  </section>

  <footer class="site-footer">
    <div class="footer-row">
      <div class="brand"><span class="brand-mark"></span>Solvik Data</div>
      <nav class="footer-nav">
        <span>Learning</span>
        <span>Blog</span>
        <span>Course Sales</span>
        <span>Subscription</span>
        <span>Sign In</span>
        <span>Sign Up</span>
      </nav>
      <div class="social" aria-label="Social links"><span></span><span></span><span></span></div>
    </div>
    <p class="copyright">Copyright © 2020 Solvik Data</p>
  </footer>
</body>
</html>
```